Psychotherapist need a business card with logo

I am a psychotherapist in need of a business card. The card must have:

Marisol Trevuneda
Psicoterapeuta
937 281 706

Psychologists use the greek letter psy, which is the psychologist symbol, but I would prefer something like a mandala, a graphic symbol, an iconic tree, nothing very usual, but something that shows confidence and trust.

Industry/Entity Type

Business

```html
<!DOCTYPE html>
<html lang="es">
<head>
<meta charset="utf-8">
<title>Marisol Trevuneda – Psicoterapeuta</title>
<link rel="stylesheet" href="https://fonts.googleapis.com/css2?family=Oxanium:wght@300;400&display=swap">
<style>
  :root {
    --backdrop: #414042;
    --card-light: #d1d2d4;
    --card-mid: #c9cacc;
    --card-dark: #a7a9ac;
    --ink: #414042;
  }
  * { margin: 0; padding: 0; box-sizing: border-box; }
  html, body {
    width: 1200px;
    height: 900px;
    overflow: hidden;
    background: var(--backdrop);
  }
  .card {
    position: absolute;
    left: 50px;
    top: 129px;
    width: 1100px;
    height: 642px;
    background: linear-gradient(90deg, var(--card-light) 0%, var(--card-light) 35%, var(--card-mid) 55%, var(--card-dark) 100%);
    font-family: "Oxanium", sans-serif;
    color: var(--ink);
  }
  .brand {
    position: absolute;
    left: 0;
    right: 0;
    top: 118px;
    display: flex;
    justify-content: center;
    align-items: center;
    gap: 16px;
    transform: translateX(30px);
  }
  .brand-dot {
    width: 22px;
    height: 22px;
    border-radius: 50%;
    background: var(--ink);
  }
  .brand-name {
    font-size: 52px;
    font-weight: 400;
    letter-spacing: 3px;
  }
  .divider {
    position: absolute;
    left: 0;
    right: 0;
    top: 284px;
    height: 10px;
    background: var(--ink);
  }
  .details {
    position: absolute;
    left: 0;
    right: 0;
    top: 350px;
    text-align: center;
  }
  .name {
    font-size: 66px;
    font-weight: 400;
    letter-spacing: 4px;
    line-height: 1;
    transform: translateX(6px);
  }
  .role {
    margin-top: 22px;
    font-size: 46px;
    font-weight: 400;
    letter-spacing: 3px;
    line-height: 1;
  }
  .phone {
    margin-top: 34px;
    font-size: 44px;
    font-weight: 300;
    letter-spacing: 2px;
    line-height: 1;
    transform: translateX(-22px);
  }
</style>
</head>
<body>
  <div class="card">
    <div class="brand">
      <span class="brand-dot"></span>
      <span class="brand-name">Raíz Serena</span>
    </div>
    <div class="divider"></div>
    <div class="details">
      <p class="name">Marisol Trevuneda</p>
      <p class="role">Psicoterapeuta</p>
      <p class="phone">937 281 706</p>
    </div>
  </div>
</body>
</html>
```